Real Estate Business Folders, Business Cards, Envelopes & Letterhead

Im looking for trendy, modern & professional design concepts for my business folder that will be used for real estate documents and property report presentations. I'm also looking for Business card designs, envelopes and letterhead with a similar theme. I have a logo already and I would like the logo colors to be incorporated in the design concepts.

Target Market(s)

Real Estate Investors, Banks, Financial Institutions

Industry/Entity Type

Real Estate

Colors
0455a3
959595
d3d3d3
848484

Requirements
Must have
• Trendy Modern, High Class look. Please include logo and colors and incorporate some silver or metallic.
• Business Address: 4812 Corvelle Blvd ste 210-300
• Alder Springs, NV 89902
• Phone: 702-555-0147
• Fax : 702-555-0183
• Email: info@mesacrestlandgroup.example
• Website: MesaCrestLandGroup.example

```html
<!DOCTYPE html>
<html lang="en">
<head>
<meta charset="utf-8">
<title>Mesa Crest Land Group — Stationery</title>
<link href="https://fonts.googleapis.com/css2?family=Open+Sans:wght@400;600;700&family=Libre+Baskerville:ital@0;1&display=swap" rel="stylesheet">
<style>
  :root {
    --brand-blue: #0455a3;
    --bright-blue: #1a7fe0;
    --navy: #0b2d5e;
    --ink: #111820;
    --silver: #959595;
    --silver-light: #d3d3d3;
    --grey: #848484;
    --paper: #ffffff;
    --stage: #c9cacc;
  }
  * { box-sizing: border-box; margin: 0; padding: 0; }
  html, body { width: 1200px; height: 872px; overflow: hidden; }
  body {
    background: radial-gradient(circle at 45% 40%, #e2e3e5 0%, var(--stage) 100%);
    font-family: "Open Sans", Arial, sans-serif;
    color: var(--ink);
    position: relative;
  }
  .sheet { position: absolute; background: var(--paper); overflow: hidden; box-shadow: 0 3px 8px rgba(0,0,0,.18); }
  .sheet--navy { background: linear-gradient(135deg, #16417f 0%, var(--navy) 100%); }
  .sheet--blue { background: linear-gradient(135deg, var(--bright-blue) 0%, var(--brand-blue) 100%); }

  .corner { position: absolute; left: 0; bottom: 0; width: 100%; height: 22%; }

  /* brand lockup */
  .brand { display: flex; align-items: center; gap: 5px; }
  .brand__mark { width: 9px; height: 9px; background: var(--brand-blue); flex: none; }
  .brand__name { font-weight: 700; color: var(--brand-blue); letter-spacing: .4px; white-space: nowrap; font-size: 9px; }
  .brand__tagline { font-family: "Libre Baskerville", Georgia, serif; font-style: italic; font-size: 5px; color: var(--grey); margin-top: 2px; white-space: nowrap; }
  .brand--light .brand__mark { background: #fff; }
  .brand--light .brand__name { color: #fff; }
  .brand--light + .brand__tagline { color: var(--silver-light); }
  .brand--lg .brand__mark { width: 18px; height: 18px; }
  .brand--lg .brand__name { font-size: 17px; }
  .brand--lg + .brand__tagline { font-size: 9px; margin-top: 4px; }
  .brand-stack--center .brand__tagline { text-align: center; }

  .contact-list { list-style: none; font-size: 4.4px; color: var(--grey); line-height: 1.9; }
  .contact-list li { display: flex; align-items: center; gap: 3px; justify-content: flex-end; white-space: nowrap; }
  .contact-list--left li { justify-content: flex-start; }
  .contact-list .dot { width: 5px; height: 5px; border-radius: 50%; background: var(--brand-blue); flex: none; }
  .contact-list--small { font-size: 3.6px; line-height: 1.8; }
  .contact-list--small .dot { width: 4px; height: 4px; }

  .addr-bar { position: absolute; right: 0; height: 10px; background: var(--brand-blue); color: #fff; font-size: 4.2px; line-height: 6px; padding: 2px 8px; text-align: right; white-space: nowrap; }

  /* header strip */
  .strip { left: 44px; top: 44px; width: 350px; height: 60px; }
  .strip .brand-wrap { position: absolute; left: 80px; top: 12px; }
  .strip .contact-list { position: absolute; right: 10px; top: 6px; }
  .strip .addr-bar { bottom: 2px; width: 62%; }

  /* letterhead */
  .letterhead { left: 54px; top: 230px; width: 282px; height: 376px; }
  .letterhead .brand-wrap { position: absolute; left: 30px; top: 32px; }
  .letter { position: absolute; left: 30px; top: 74px; right: 26px; font-size: 4.6px; line-height: 1.55; color: #333; }
  .letter__to { margin-bottom: 6px; }
  .letter__to strong { color: var(--brand-blue); font-weight: 600; }
  .letter__date { position: absolute; right: 0; top: 14px; }
  .letter p { margin-bottom: 6px; }
  .letter__sign { margin-top: 10px; }
  .letter__sign strong { font-size: 5.2px; }
  .letterhead .contact-list { position: absolute; right: 12px; bottom: 36px; }
  .letterhead .addr-bar { bottom: 12px; width: 58%; }

  /* notebook / folder cover */
  .cover { left: 455px; top: 44px; width: 228px; height: 288px; }
  .cover .brand-wrap { position: absolute; left: 0; right: 0; top: 112px; display: flex; justify-content: center; }
  .cover .band { position: absolute; right: 0; bottom: 14px; width: 55%; height: 6px; background: var(--bright-blue); }
  .cover .band--dark { bottom: 8px; width: 100%; height: 6px; background: #071b3a; }

  /* business cards */
  .card { width: 148px; height: 76px; left: 360px; }
  .card--front { top: 430px; }
  .card--back { top: 522px; }
  .card .brand__mark { width: 6px; height: 6px; }
  .card .brand__name { font-size: 6px; }
  .card--front .brand-wrap { position: absolute; left: 12px; top: 10px; }
  .card--front .contact-list { position: absolute; left: 12px; top: 32px; }
  .card__person { position: absolute; left: 66px; top: 34px; font-size: 5px; }
  .card__person strong { display: block; color: var(--brand-blue); font-weight: 700; }
  .card__person span { font-size: 3.6px; color: var(--grey); }
  .card--back .brand-wrap { position: absolute; right: 12px; top: 28px; }

  /* report cover sheet */
  .report { left: 540px; top: 424px; width: 176px; height: 172px; }
  .report .brand-wrap { position: absolute; left: 12px; top: 14px; }

  /* envelopes */
  .envelope { left: 54px; top: 688px; width: 282px; height: 140px; }
  .envelope .brand-wrap { position: absolute; left: 16px; top: 14px; }
  .envelope .contact-list { position: absolute; left: 16px; top: 62px; }
  .envelope .window { position: absolute; right: 22px; top: 48px; width: 96px; height: 42px; border: 1px solid var(--silver-light); background: #f4f5f7; }
  .envelope-back { left: 380px; top: 648px; width: 272px; height: 180px; }
  .envelope-back .flap { position: absolute; left: 0; top: 0; width: 100%; height: 58%; }
  .envelope-back .web { position: absolute; left: 0; right: 0; bottom: 16px; text-align: center; font-size: 5.4px; font-weight: 600; color: var(--brand-blue); }

  /* presentation folder */
  .folder { left: 868px; top: 446px; width: 292px; height: 388px; }
  .folder .brand-wrap { position: absolute; left: 0; right: 0; top: 150px; display: flex; justify-content: center; }
</style>
</head>
<body>

  <!-- header strip -->
  <section class="sheet strip">
    <svg class="corner" viewBox="0 0 100 40" preserveAspectRatio="none" style="height:100%"><polygon points="0,0 12,0 20,40 0,40" fill="#1a7fe0"/><polygon points="0,14 7,14 13,40 0,40" fill="#0455a3"/><rect x="0" y="36" width="100" height="4" fill="#111820"/></svg>
    <div class="brand-wrap"><div class="brand"><span class="brand__mark"></span><span class="brand__name">MESA CREST LAND GROUP</span></div><p class="brand__tagline">"Building Value Together"</p></div>
    <ul class="contact-list"><li>702-555-0147<span class="dot"></span></li><li>702-555-0183<span class="dot"></span></li><li>info@mesacrestlandgroup.example<span class="dot"></span></li><li>MesaCrestLandGroup.example<span class="dot"></span></li></ul>
    <div class="addr-bar">4812 Corvelle Blvd ste 210-300, Alder Springs, NV 89902</div>
  </section>

  <!-- letterhead -->
  <section class="sheet letterhead">
    <div class="brand-wrap"><div class="brand"><span class="brand__mark"></span><span class="brand__name">MESA CREST LAND GROUP</span></div><p class="brand__tagline">"Building Value Together"</p></div>
    <div class="letter">
      <div class="letter__to"><strong>Laura Finch</strong><br>Client Director<br>14 Harlow Road, Suite 9</div>
      <div class="letter__date">Date: 30 March, 2024</div>
      <p>Thank you for meeting with our team last week to review the property portfolio and the market report.</p>
      <p>We have prepared a detailed valuation for each listing, along with comparable sales in the surrounding area.</p>
      <p>Please review the attached summary and let us know which properties you would like to discuss further.</p>
      <p>We look forward to working together on your next investment.</p>
      <div class="letter__sign"><strong>Daniel Reyes</strong><br>Manager</div>
    </div>
    <ul class="contact-list"><li>702-555-0147<span class="dot"></span></li><li>702-555-0183<span class="dot"></span></li><li>info@mesacrestlandgroup.example<span class="dot"></span></li><li>MesaCrestLandGroup.example<span class="dot"></span></li></ul>
    <div class="addr-bar">4812 Corvelle Blvd ste 210-300, Alder Springs, NV 89902</div>
    <svg class="corner" viewBox="0 0 100 60" preserveAspectRatio="none"><polygon points="0,0 22,60 0,60" fill="#1a7fe0"/><polygon points="0,24 12,60 0,60" fill="#0455a3"/><rect x="0" y="56" width="100" height="4" fill="#111820"/></svg>
  </section>

  <!-- cover -->
  <section class="sheet sheet--navy cover">
    <div class="brand-wrap"><div class="brand-stack--center"><div class="brand brand--light"><span class="brand__mark"></span><span class="brand__name">MESA CREST LAND GROUP</span></div><p class="brand__tagline">"Building Value Together"</p></div></div>
    <div class="band"></div><div class="band band--dark"></div>
  </section>

  <!-- business cards -->
  <section class="sheet card card--front">
    <div class="brand-wrap"><div class="brand"><span class="brand__mark"></span><span class="brand__name">MESA CREST LAND GROUP</span></div></div>
    <ul class="contact-list contact-list--left contact-list--small"><li><span class="dot"></span>702-555-0147</li><li><span class="dot"></span>702-555-0183</li><li><span class="dot"></span>Alder Springs, NV</li></ul>
    <div class="card__person"><strong>OWEN HALE CARTER</strong><span>Acquisitions Director</span></div>
    <svg class="corner" viewBox="0 0 100 30" preserveAspectRatio="none" style="height:30%"><polygon points="0,0 16,30 0,30" fill="#1a7fe0"/><rect x="0" y="26" width="100" height="4" fill="#111820"/><rect x="60" y="22" width="40" height="4" fill="#0455a3"/></svg>
  </section>
  <section class="sheet sheet--blue card card--back">
    <div class="brand-wrap"><div class="brand brand--light"><span class="brand__mark"></span><span class="brand__name">MESA CREST LAND GROUP</span></div></div>
    <svg class="corner" viewBox="0 0 100 30" preserveAspectRatio="none" style="height:30%"><polygon points="0,0 20,30 0,30" fill="#0b2d5e"/><rect x="0" y="26" width="100" height="4" fill="#111820"/></svg>
  </section>

  <!-- report sheet -->
  <section class="sheet report">
    <div class="brand-wrap"><div class="brand"><span class="brand__mark"></span><span class="brand__name">MESA CREST LAND GROUP</span></div><p class="brand__tagline">"Building Value Together"</p></div>
    <svg class="corner" viewBox="0 0 100 40" preserveAspectRatio="none"><polygon points="0,0 20,40 0,40" fill="#1a7fe0"/><polygon points="0,16 11,40 0,40" fill="#0455a3"/><rect x="0" y="36" width="100" height="4" fill="#111820"/><rect x="55" y="32" width="45" height="4" fill="#0455a3"/></svg>
  </section>

  <!-- envelope front -->
  <section class="sheet envelope">
    <div class="brand-wrap"><div class="brand"><span class="brand__mark"></span><span class="brand__name">MESA CREST LAND GROUP</span></div><p class="brand__tagline">"Building Value Together"</p></div>
    <ul class="contact-list contact-list--left"><li><span class="dot"></span>702-555-0147</li><li><span class="dot"></span>702-555-0183</li><li><span class="dot"></span>info@mesacrestlandgroup.example</li><li><span class="dot"></span>MesaCrestLandGroup.example</li><li><span class="dot"></span>4812 Corvelle Blvd ste 210-300, Alder Springs, NV 89902</li></ul>
    <div class="window"></div>
    <svg class="corner" viewBox="0 0 100 30" preserveAspectRatio="none"><polygon points="0,4 12,30 0,30" fill="#1a7fe0"/><rect x="0" y="27" width="100" height="3" fill="#111820"/><rect x="62" y="24" width="38" height="3" fill="#0455a3"/></svg>
  </section>

  <!-- envelope back -->
  <section class="sheet envelope-back">
    <svg class="flap" viewBox="0 0 100 60" preserveAspectRatio="none"><defs><linearGradient id="flapFill" x1="0" y1="0" x2="0" y2="1"><stop offset="0" stop-color="#16417f"/><stop offset="1" stop-color="#0b2d5e"/></linearGradient></defs><path d="M0,0 H100 V30 Q50,70 0,30 Z" fill="url(#flapFill)"/></svg>
    <p class="web">MesaCrestLandGroup.example</p>
  </section>

  <!-- presentation folder -->
  <section class="sheet folder">
    <div class="brand-wrap"><div class="brand-stack--center"><div class="brand brand--lg"><span class="brand__mark"></span><span class="brand__name">MESA CREST LAND GROUP</span></div><p class="brand__tagline">"Building Value Together"</p></div></div>
    <svg class="corner" viewBox="0 0 100 40" preserveAspectRatio="none" style="height:16%"><polygon points="0,0 22,40 0,40" fill="#1a7fe0"/><polygon points="0,14 13,40 0,40" fill="#0455a3"/><rect x="0" y="36" width="100" height="4" fill="#111820"/><rect x="30" y="31" width="70" height="5" fill="#0455a3"/></svg>
  </section>

</body>
</html>
```